Livestock Consulting Company has a logo but needs business cards and a uniform logo

My company works with farmers advising them on managing cattle and sheep. I have a logo but need business cards and a version of my logo to go onto my work shirts. I need the following wording added to my logo for my shirts "Tallowby Livestock Consulting".

```html
<!DOCTYPE html>
<html lang="en">
<head>
<meta charset="utf-8">
<title>Tallowby Livestock Consulting – Business Card</title>
<link rel="stylesheet" href="https://fonts.googleapis.com/css2?family=Roboto+Condensed:wght@400;700&family=Arimo:wght@400&display=swap">
<style>
  :root {
    --stage: #2a2a2a;
    --card: #ffffff;
    --brand-brown: #7a5a3a;
    --back-brown: #7d6044;
    --back-light: #a3825d;
    --back-dark: #4a3625;
    --text-grey: #555555;
    --rule: #a58a6c;
  }
  html, body {
    margin: 0;
    padding: 0;
    width: 1200px;
    height: 960px;
    overflow: hidden;
    background: var(--stage);
  }
  .canvas {
    position: relative;
    width: 1200px;
    height: 960px;
  }
  .card {
    position: absolute;
    width: 740px;
    height: 400px;
    box-shadow: 0 18px 40px rgba(0,0,0,0.55);
    overflow: hidden;
  }
  .card-back {
    left: 60px;
    top: 90px;
    background: linear-gradient(135deg, var(--back-light) 0%, var(--back-brown) 50%, var(--back-dark) 100%);
  }
  .card-front {
    left: 420px;
    top: 470px;
    background: var(--card);
    font-family: "Arimo", sans-serif;
    color: var(--text-grey);
  }
  .brand {
    position: absolute;
    right: 48px;
    top: 58px;
    display: flex;
    align-items: center;
    gap: 12px;
  }
  .brand-dot {
    width: 22px;
    height: 22px;
    border-radius: 50%;
    background: var(--brand-brown);
  }
  .brand-name {
    font-family: "Roboto Condensed", sans-serif;
    font-weight: 700;
    font-size: 24px;
    letter-spacing: 0.5px;
    text-transform: uppercase;
    color: var(--brand-brown);
  }
  .rule {
    position: absolute;
    height: 1px;
    background: var(--rule);
  }
  .rule-main { left: 60px; right: 48px; top: 200px; }
  .rule-name { left: 60px; width: 220px; top: 296px; }
  .person {
    position: absolute;
    left: 60px;
    top: 222px;
  }
  .person-name {
    font-family: "Roboto Condensed", sans-serif;
    font-weight: 700;
    font-size: 30px;
    color: var(--brand-brown);
    margin: 0;
    line-height: 1.1;
    white-space: nowrap;
  }
  .person-title {
    font-size: 17px;
    margin: 4px 0 0 6px;
  }
  .address {
    position: absolute;
    left: 72px;
    top: 314px;
    font-size: 20px;
    line-height: 1.35;
    font-style: normal;
    white-space: nowrap;
  }
  .contacts {
    position: absolute;
    top: 232px;
    list-style: none;
    margin: 0;
    padding: 0;
    line-height: 1.5;
    white-space: nowrap;
  }
  .contacts li { display: flex; align-items: center; gap: 8px; }
  .contacts svg { width: 15px; height: 15px; fill: var(--brand-brown); flex: none; }
  .contacts-phone { left: 300px; font-size: 18px; }
  .contacts-web { right: 48px; font-size: 15px; top: 234px; }
</style>
</head>
<body>
<main class="canvas">
  <div class="card card-back" role="img" aria-label="Card back with a repeating embossed monogram pattern in gold and dark brown tones"></div>

  <section class="card card-front">
    <div class="brand">
      <span class="brand-dot"></span>
      <span class="brand-name">Tallowby Livestock Consulting</span>
    </div>

    <div class="rule rule-main"></div>

    <div class="person">
      <h1 class="person-name">DANIEL HARLOW</h1>
      <p class="person-title">President</p>
    </div>

    <div class="rule rule-name"></div>

    <address class="address">1420 Fernbrook Road<br>Fairbanks, Alaska 34810</address>

    <ul class="contacts contacts-phone">
      <li>
        <svg viewBox="0 0 16 16" aria-hidden="true"><path d="M2 5c0-2 2-3 6-3s6 1 6 3v1h-3V5H5v1H2zM4 7h8l2 7H2z"/></svg>
        369-555-0142
      </li>
      <li>
        <svg viewBox="0 0 16 16" aria-hidden="true"><path d="M4 1h8a1 1 0 0 1 1 1v12a1 1 0 0 1-1 1H4a1 1 0 0 1-1-1V2a1 1 0 0 1 1-1zm1 2v9h6V3z"/></svg>
        369-555-0187
      </li>
    </ul>

    <ul class="contacts contacts-web">
      <li>
        <svg viewBox="0 0 16 16" aria-hidden="true"><path d="M1 3h14v10H1zm1 1.5V5l6 4 6-4v-.5z"/></svg>
        info@tallowbylivestock.com
      </li>
      <li>
        <svg viewBox="0 0 16 16" aria-hidden="true"><circle cx="8" cy="8" r="7"/></svg>
        www.tallowbylivestock.com
      </li>
    </ul>
  </section>
</main>
</body>
</html>
```